Cannabis packaging label for a medicine bottle

This label will be for packaged cannabis. There are certain regulations that I will need incorporated such as warning symbols and mandatory wording on the label. The label will be for a medicine canister the measurements are 2 x 4.75. The primary photo will be in the center of the label. Please see photos attached of example label and also a photo of the container.

Product name: “Vela Pine”.....”Cannabis Flower”...”California Grown”

Target Market(s)

Young and older adults with a conservative sophisticated feel.

Font styles to use
Serif

Colors

Designer to choose colors to be used in the design.

Requirements
Must have
• Primary panel is the part of a cannabis product label that is most likely to be displayed, presented, shown, or examined under customary conditions of display for retail sale.
• Informational panel is any part of the cannabis product label that is not the primary panel and that contains required labeling information.
• All labels must be unobstructed and conspicuous, so the consumer can easily read the labels. The required information shall be located on the outside container or wrapper of the finished product and must have the following information, in no less that 6-point font.
• Primary Panel – All Products:
• Identity of product.
• Universal symbol (must be in black and white).
• Net weight 3.5 grams or volume of the contents in the package.
• Informational Panel – All Products:
• The applicable Government Warning.
• The CA Universal Symbol )may be no smaller than half (.5) inch by x half (.5) inch.)
• This is the applicable government warning for all flower products.
• Primary Panel – Manufactured Goods:
• The THC/CBD contents for the entire contents of the package in milligrams.
• Informational Panel – Manufactured Goods:
• Licensed manufacturer name and contact phone number or web address.
Nice to have
• Modern design but you and hip. Spray paint mame “Vela Pine”
Should not have
• Should not be appealing to children

```html
<!DOCTYPE html>
<html lang="en">
<head>
<meta charset="utf-8">
<title>Vela Pine – Cannabis Flower Label</title>
<link rel="stylesheet" href="https://fonts.googleapis.com/css2?family=Bangers&family=Archivo+Black&family=Open+Sans:wght@400;600;700&display=swap">
<style>
  :root {
    --page: #ffffff;
    --green: #31c41c;
    --green-deep: #26ad14;
    --yellow: #ffe600;
    --black: #0d0d0d;
    --panel: rgba(255, 255, 255, 0.22);
    --banner-text: #3ed21f;
  }
  * { box-sizing: border-box; margin: 0; padding: 0; }
  html, body {
    width: 1200px; height: 610px; overflow: hidden;
    background: var(--page);
  }
  .label {
    position: absolute; left: 255px; top: 164px;
    width: 690px; height: 291px;
    box-shadow: 3px 4px 6px rgba(0,0,0,0.25);
    overflow: hidden;
  }
  .label-field {
    position: absolute; inset: 0;
    background: linear-gradient(180deg, var(--green) 0%, var(--green-deep) 100%);
  }
  .band { position: absolute; left: 0; right: 0; }
  .band-yellow-top { top: 0; height: 5px; background: var(--yellow); }
  .band-black-top { top: 5px; height: 8px; background: var(--black); }
  .band-black-bottom { top: 278px; height: 8px; background: var(--black); }
  .band-yellow-bottom { top: 286px; height: 5px; background: var(--yellow); }

  .brand-name {
    position: absolute; left: 22px; top: 38px;
    font-family: 'Bangers', cursive;
    font-size: 60px; line-height: 1; letter-spacing: 2px;
    color: var(--yellow);
  }
  .product-banner {
    position: absolute; left: 32px; top: 124px;
    width: 250px; height: 50px;
    transform: rotate(-3deg);
  }
  .product-banner::before {
    content: ""; position: absolute; left: -6px; top: 6px;
    width: 250px; height: 50px; background: var(--yellow);
  }
  .product-banner-fill {
    position: absolute; inset: 0; background: var(--black);
    display: flex; align-items: center; justify-content: center;
    font-family: 'Bangers', cursive; font-size: 27px; letter-spacing: 1px;
    color: var(--banner-text);
  }
  .origin, .net-weight {
    position: absolute;
    font-family: 'Archivo Black', sans-serif;
    color: var(--black);
    font-size: 14px; letter-spacing: 0.3px;
  }
  .origin { left: 62px; top: 197px; }
  .net-weight { left: 56px; top: 254px; }
  .universal-symbol { position: absolute; left: 234px; top: 196px; }

  .warning-panel {
    position: absolute; left: 386px; top: 13px;
    width: 274px; height: 211px;
    background: var(--panel); border-radius: 8px;
    padding: 6px 10px 0 10px;
    font-family: 'Open Sans', sans-serif;
    font-size: 11.4px; line-height: 16.2px;
    text-align: justify; text-transform: uppercase;
    color: var(--black);
  }
  .warning-panel strong { font-weight: 700; }
  .maker-info {
    position: absolute; left: 396px; top: 229px;
    font-family: 'Open Sans', sans-serif; font-weight: 600;
    font-size: 9.6px; line-height: 12.6px;
    color: var(--black);
  }
</style>
</head>
<body>
  <div class="label">
    <div class="label-field" role="img" aria-label="Green painted brick wall background"></div>
    <div class="band band-yellow-top"></div>
    <div class="band band-black-top"></div>
    <div class="band band-black-bottom"></div>
    <div class="band band-yellow-bottom"></div>

    <div class="brand-name">VELA PINE</div>

    <div class="product-banner">
      <div class="product-banner-fill">CANNABIS FLOWER</div>
    </div>

    <div class="origin">CALIFORNIA GROWN</div>
    <div class="net-weight">NET WEIGHT 3.5 GRAMS</div>

    <svg class="universal-symbol" width="50" height="46" viewBox="0 0 50 46" aria-label="Universal cannabis symbol">
      <path d="M25 3 L47 42 L3 42 Z" fill="none" stroke="#0d0d0d" stroke-width="4" stroke-linejoin="round"/>
    </svg>

    <div class="warning-panel">
      <strong>Government warning:</strong> This package contains cannabis, a schedule controlled substance. Keep out of reach of children and animals. Cannabis may only be possessed or consumed by persons 21 years of age or older unless the person is a qualified patient. Cannabis use while pregnant or breastfeeding may be harmful. Consumption of cannabis impairs your ability to drive and operate machinery. Please use extreme caution.
    </div>

    <div class="maker-info">
      Manufactured by:<br>
      Contact Number<br>
      www.webaddress.com
    </div>
  </div>
</body>
</html>
```